Business Card and Letterhead Design for Public Accounting Firm

Business card and letterhead design for a CPA Firm located in Orange County, CA. We're looking for a modern and professional design utilizing our existing logo. We'd like a clean "less is more" look, but also something that catches the eye. We provide a high level of service to our clients. Open to single or double sided business cards.

Additional info: color numbers on logo
Blue :
R 0
G 83
B 125

#00537D

Silver :

R 154
G 154
B 154

#9A9A9A

Target Market(s)

Businesses and individuals

Industry/Entity Type

Accounting

Contact Information for Business Card

Moss Whitfield & Danby LLP - 4827 Larkspur Vale Road, Irvine, CA 92614 - (949)731-2864 - mwdaccts.example

Font styles to use
Serif
Sans Serif
Other font styles liked:
• See font file uploaded

Colors
0054AA
0677BA
7BADD7
CADEEF
E8F1F8

Requirements
Nice to have
• Possibly use the font file provided which matches our logo, but adjust to be not in all caps

```html
<!DOCTYPE html>
<html lang="en">
<head>
<meta charset="utf-8">
<title>Moss Whitfield &amp; Danby LLP — Stationery</title>
<link rel="stylesheet" href="https://fonts.googleapis.com/css2?family=Tinos&display=swap">
<style>
  :root {
    --brand-blue: #03567f;
    --brand-blue-deep: #024a6e;
    --brand-blue-light: #0a6a98;
    --silver: #9a9a9a;
    --paper: #ffffff;
    --backdrop: #c1c9ce;
    --ink-light: #ffffff;
    --ink-dark: #222222;
  }
  * { box-sizing: border-box; margin: 0; padding: 0; }
  html, body {
    width: 1140px; height: 1200px; overflow: hidden;
    background: var(--backdrop);
    font-family: "Tinos", "Times New Roman", serif;
  }
  .canvas { position: relative; width: 1140px; height: 1200px; }

  .sheet {
    position: absolute;
    box-shadow: 1px 2px 3px rgba(0,0,0,.35);
    overflow: hidden;
  }
  .firm-name {
    position: absolute;
    color: var(--brand-blue);
    text-transform: uppercase;
    letter-spacing: .12em;
    line-height: 1.2;
    font-weight: 400;
    white-space: nowrap;
  }
  .firm-name--light { color: var(--ink-light); }

  /* Business card front */
  .card-front { left: 36px; top: 84px; width: 520px; height: 298px; background: var(--paper); }
  .card-front .firm-name { left: 30px; top: 36px; font-size: 17px; }
  .card-front .silver-band { position: absolute; left: 0; top: 154px; width: 100%; height: 6px; background: var(--silver); }
  .card-front .blue-panel { position: absolute; left: 0; top: 162px; width: 100%; height: 136px; background: var(--brand-blue); color: var(--ink-light); }
  .contact-list { position: absolute; left: 30px; top: 28px; list-style: none; font-size: 14px; white-space: nowrap; }
  .contact-list li { display: flex; align-items: center; height: 29px; }
  .contact-list svg { width: 10px; height: 10px; margin-right: 5px; fill: var(--ink-light); flex: none; }
  .card-address {
    position: absolute; left: 331px; top: 74px;
    border-left: 1px solid var(--ink-light);
    padding-left: 5px; font-size: 14px; line-height: 1.25; white-space: nowrap;
  }

  /* Backs */
  .card-back { left: 577px; top: 84px; width: 520px; height: 298px; background: var(--brand-blue); }
  .letter-back { left: 574px; top: 418px; width: 520px; height: 736px; background: var(--brand-blue); }
  .tone-field {
    position: absolute; inset: 0;
    background: linear-gradient(135deg, var(--brand-blue-deep) 0%, var(--brand-blue) 50%, var(--brand-blue-light) 100%);
    opacity: .55;
  }
  .card-back .firm-name { left: 344px; top: 245px; font-size: 10px; }
  .letter-back .firm-name { left: 342px; top: 670px; font-size: 10px; }

  /* Letterhead */
  .letterhead { left: 36px; top: 418px; width: 520px; height: 736px; background: var(--paper); }
  .letterhead .firm-name { left: 39px; top: 36px; font-size: 19px; }
  .letterhead-footer { position: absolute; left: 0; top: 0; width: 520px; height: 736px; }
  .footer-contacts {
    position: absolute; left: 38px; top: 648px;
    display: flex; gap: 8px; font-size: 9px; color: var(--ink-dark); white-space: nowrap;
  }
  .footer-contacts span { display: flex; align-items: center; }
  .footer-contacts svg { width: 7px; height: 7px; margin-right: 3px; flex: none; }
  .footer-address {
    position: absolute; left: 352px; top: 678px;
    color: var(--ink-light); font-size: 12px; line-height: 1.25; white-space: nowrap;
  }
</style>
</head>
<body>
<main class="canvas">

  <section class="sheet card-front" aria-label="Business card, front">
    <p class="firm-name">Moss Whitfield<br>&amp; Danby LLP</p>
    <div class="silver-band"></div>
    <div class="blue-panel">
      <ul class="contact-list">
        <li><svg viewBox="0 0 10 10"><path d="M2 0.5 L3.6 2.8 L2.7 3.8 Q3.8 6 6.2 7.3 L7.2 6.4 L9.5 8 L8.4 9.5 Q4.5 9.4 0.5 1.6 Z"/></svg>(949)731-2864</li>
        <li><svg viewBox="0 0 10 10"><path d="M0.5 2 H9.5 V8 H0.5 Z M1 2.5 L5 5.5 L9 2.5" fill="none" stroke="#fff" stroke-width="1"/></svg>cpa@mwdaccts.example</li>
        <li><svg viewBox="0 0 10 10"><g fill="none" stroke="#fff" stroke-width=".8"><circle cx="5" cy="5" r="4.3"/><ellipse cx="5" cy="5" rx="1.8" ry="4.3"/><path d="M0.7 5 H9.3 M1.5 2.7 H8.5 M1.5 7.3 H8.5"/></g></svg>www.mwdaccts.example</li>
      </ul>
      <p class="card-address">4827 Larkspur Vale Road,<br>Irvine, California 92614</p>
    </div>
  </section>

  <section class="sheet card-back" aria-label="Business card, back">
    <div class="tone-field" role="img" aria-label="Tonal blue background with a repeating firm-name pattern"></div>
    <p class="firm-name firm-name--light">Moss Whitfield<br>&amp; Danby LLP</p>
  </section>

  <section class="sheet letterhead" aria-label="Letterhead">
    <p class="firm-name">Moss Whitfield<br>&amp; Danby LLP</p>
    <svg class="letterhead-footer" viewBox="0 0 520 736" aria-hidden="true">
      <polyline points="0,673 320,673 335,633 520,633" fill="none" stroke="#9a9a9a" stroke-width="6"/>
      <polygon points="0,683 326,683 341,643 520,643 520,736 0,736" fill="#03567f"/>
    </svg>
    <div class="footer-contacts">
      <span><svg viewBox="0 0 10 10"><path fill="#03567f" d="M2 0.5 L3.6 2.8 L2.7 3.8 Q3.8 6 6.2 7.3 L7.2 6.4 L9.5 8 L8.4 9.5 Q4.5 9.4 0.5 1.6 Z"/></svg>(949)731-2864</span>
      <span><svg viewBox="0 0 10 10"><path d="M0.5 2 H9.5 V8 H0.5 Z M1 2.5 L5 5.5 L9 2.5" fill="none" stroke="#03567f" stroke-width="1.2"/></svg>cpa@mwdaccts.example</span>
      <span><svg viewBox="0 0 10 10"><g fill="none" stroke="#03567f" stroke-width="1"><circle cx="5" cy="5" r="4.3"/><ellipse cx="5" cy="5" rx="1.8" ry="4.3"/><path d="M0.7 5 H9.3"/></g></svg>www.mwdaccts.example</span>
    </div>
    <p class="footer-address">4827 Larkspur Vale Road,<br>Irvine, California 92614</p>
  </section>

  <section class="sheet letter-back" aria-label="Letterhead, back">
    <div class="tone-field" role="img" aria-label="Tonal blue background with a repeating firm-name pattern"></div>
    <p class="firm-name firm-name--light">Moss Whitfield<br>&amp; Danby LLP</p>
  </section>

</main>
</body>
</html>
```